need professional, precise design for a website

I will start with a homepage design and if we pick your design, we'll have you design up to 6 more interior pages (we'll pay extra for these of course). We need a homepage design for a reserve study company based in Idaho, covering the northwest region. The company is called copper ridge reserve study. Their current site is at https://www.copperridgereserves.example/ and they really like this site for inspiration https://www.fundplannerhub.example/ but they would like an original design, just more modern and fresh like the sample site. I have logo files I will attach. They want something that looks financial and has a feel of accuity. Their main call to action will be to have someone fill in a contact form or call them on the phone. They will have a sample study that someone can download as on the fundplannerhub site. You can use copy from their current site.

```html
<!DOCTYPE html>
<html lang="en">
<head>
<meta charset="utf-8">
<title>Copper Ridge Reserves</title>
<link href="https://fonts.googleapis.com/css2?family=Noto+Serif:wght@700&family=Roboto:wght@400;500&family=Mulish:wght@600&display=swap" rel="stylesheet">
<style>
  :root{
    --gold:#e6bc6a;
    --gold-text:#d3a552;
    --ink:#111418;
    --heading:#1d2430;
    --body:#5c6066;
    --white:#ffffff;
    --sky-top:#3d5a86;
    --sky-mid:#6c8cbc;
    --wall:#c9d2e0;
  }
  *{margin:0;padding:0;box-sizing:border-box}
  html,body{width:1200px;height:1199px;overflow:hidden;background:var(--white)}
  body{position:relative;font-family:'Roboto',sans-serif}
  .hero{position:absolute;left:0;top:0;width:1200px;height:564px;overflow:hidden}
  .hero-photo{position:absolute;inset:0;
    background:linear-gradient(180deg,var(--sky-top) 0%,var(--sky-mid) 30%,var(--wall) 55%,#9fadc4 80%,#55623f 100%)}
  .hero-shade{position:absolute;inset:0;background:linear-gradient(180deg,rgba(20,30,50,.35),rgba(20,30,50,.1) 40%,rgba(20,30,50,.15))}
  .nav{position:absolute;top:22px;left:0;width:1200px;height:20px;font-family:'Noto Serif',serif;font-weight:700;font-size:9.6px;color:var(--white)}
  .nav a{position:absolute;color:var(--white);text-decoration:none;top:0}
  .nav a.active{color:var(--gold)}
  .nav a.active::after{content:"";position:absolute;left:0;top:15px;width:13px;height:2px;background:var(--gold)}
  .brand{position:absolute;left:507px;top:17px;display:flex;align-items:center;gap:6px;font-family:'Noto Serif',serif;font-weight:700;font-size:11.5px;color:var(--white);letter-spacing:.2px}
  .brand-mark{width:14px;height:14px;border:2px solid var(--white);border-radius:50%}
  .hero-title{position:absolute;left:0;top:248px;width:1170px;text-align:center;font-family:'Noto Serif',serif;font-weight:700;font-size:42px;line-height:56px;color:var(--white)}
  .btn{position:absolute;left:526px;top:419px;width:119px;height:38px;background:var(--gold);color:var(--white);font-size:11.5px;font-weight:500;display:flex;align-items:center;justify-content:center;text-decoration:none}
  .dots{position:absolute;top:523px;left:558px;display:flex;gap:8px}
  .dots span{width:13px;height:13px;border:2px solid var(--white);border-radius:50%}
  .dots span.on{background:var(--white)}
  .intro-title{position:absolute;left:154px;top:676px;font-family:'Noto Serif',serif;font-weight:700;font-size:31px;line-height:45px;color:var(--ink)}
  .rule{position:absolute;left:154px;top:793px;width:38px;height:3px;background:var(--gold)}
  .intro-text{position:absolute;left:154px;top:844px;width:292px;font-size:12.2px;line-height:26.4px;color:var(--body)}
  .read-more{position:absolute;left:154px;top:1122px;font-size:9.6px;font-weight:500;color:var(--gold-text);text-decoration:none;display:flex;align-items:center;gap:5px}
  .read-more::after{content:"";width:24px;height:1px;background:var(--gold-text)}
  .service{position:absolute;width:210px}
  .service svg{display:block;width:66px;height:70px}
  .service h3{margin-top:36px;font-family:'Mulish',sans-serif;font-weight:600;font-size:16px;line-height:22px;color:var(--heading)}
  .service p{margin-top:11px;font-size:12.2px;line-height:19.5px;color:var(--body)}
</style>
</head>
<body>
<header class="hero">
  <div class="hero-photo" role="img" aria-label="Modern white multi-level villa with glass balconies under a blue sky"></div>
  <div class="hero-shade"></div>
  <nav class="nav">
    <a class="active" style="left:118px" href="#">About</a>
    <a style="left:165px" href="#">Location &amp; Lifestyle</a>
    <a style="left:274px" href="#">Design</a>
    <a style="left:841px" href="#">Resources</a>
    <a style="left:908px" href="#">Get In Touch</a>
    <a style="left:998px" href="#">Client Portal</a>
  </nav>
  <div class="brand"><span class="brand-mark"></span>Copper Ridge Reserves</div>
  <h1 class="hero-title">Prior Proper Planning Prevents Poor<br>Performance!</h1>
  <a class="btn" href="#">LEARN MORE</a>
  <div class="dots"><span class="on"></span><span></span><span></span></div>
</header>

<main>
  <h2 class="intro-title">Your financial road map<br>for the next 30 years!</h2>
  <div class="rule"></div>
  <p class="intro-text">A copper ridge is a constant on the skyline that travelers have relied on for generations.&nbsp; Navigating these trails is simply knowing the right points of origin and following the map that the land has laid before us. We love the high country!&nbsp; Amidst so much wilderness and a seemingly chaotic expanse of peaks and valleys, there is great order.&nbsp; Of all the ridges and distractions of the beautiful range.</p>
  <a class="read-more" href="#">Read More</a>

  <section class="service" style="left:630px;top:715px">
    <svg viewBox="0 0 66 70" fill="none" stroke="var(--gold)" stroke-width="2"><rect x="18" y="3" width="28" height="64"/><rect x="3" y="36" width="20" height="31"/><rect x="44" y="26" width="19" height="41"/><path d="M24 12h4M31 12h4M38 12h4M24 22h4M31 22h4M38 22h4M24 32h4M31 32h4M38 32h4M8 46h4M14 46h4M8 56h4M14 56h4M49 36h9M49 46h9M49 56h9M1 68h64"/></svg>
    <h3>HOA &amp; Condominium<br>Studies</h3>
    <p>An usu virtute vocibus, per nullam primis ea fugit paulo namapa</p>
  </section>

  <section class="service" style="left:879px;top:716px">
    <svg viewBox="0 0 66 70" fill="none" stroke="var(--gold)" stroke-width="2"><path d="M8 14h50v52H8zM4 14l10-9h38l10 9M28 5l5-4 5 4M14 26h8v10h-8zM29 26h8v10h-8zM44 26h8v10h-8zM14 48h8v18h-8zM29 48h8v18h-8zM44 48h8v10h-8zM1 67h64"/></svg>
    <h3>Commercial, Vacation &amp;<br>Time Share</h3>
    <p>An usu virtute vocibus, per nullam primis ea fugit paulo namapa</p>
  </section>

  <section class="service" style="left:629px;top:934px">
    <svg viewBox="0 0 66 70" fill="none" stroke="var(--gold)" stroke-width="2"><path d="M10 6h46v56H10zM6 6h54M16 16h7v9h-7zM29 16h7v9h-7zM42 16h7v9h-7zM16 32h7v9h-7zM29 32h7v9h-7zM42 32h7v9h-7zM16 48h7v14h-7zM29 48h9v14h-9zM42 48h7v8h-7zM3 63h60"/></svg>
    <h3>Parks &amp; Public<br>Lands</h3>
    <p>An usu virtute vocibus, per nullam primis ea fugit paulo namapa</p>
  </section>

  <section class="service" style="left:878px;top:935px">
    <svg viewBox="0 0 66 70" fill="none" stroke="var(--gold)" stroke-width="2"><path d="M26 3h30v62H26zM32 12h5M44 12h5M32 24h5M44 24h5M32 36h5M44 36h5M44 48h5M4 46l15-12 16 12M8 43v22h25V43M14 54h7v11h-7zM1 66h64"/></svg>
    <h3>Condo<br>Reserves</h3>
    <p>An usu virtute vocibus, per nullam primis ea fugit paulo namapa</p>
  </section>
</main>
</body>
</html>
```